Business card design for a dynamic IT consulting company

We need a business card design for a young firm, specialized in the Telecommunications/Consulting industry. The name of the company is Brask and Partners Business Consulting Ltd. (Short name: Brask and Partnes)
Brask = solve read reverse, so we aim to be uncomplicated and solution-oriented. The small pipe in our logo is also related to the word solve. So we need a new business card design, which is simple, eye catching and something non traditional (I would probably prefer a square shaped design rather than a rectangle, but open for suggestions). Attached our logo.

Target Market(s)

Usually our customers are Tier1 Telecoms providers (Q-Linkra, Parnexo, etc) and their executives.

Industry/Entity Type

Business

Contact Information for Business Card

Name: Gergely Halmindo
Email: g.halmindo@braskpartnera.hu
Web: www.braskpartnera.hu
Mobile: +36 30 555 0192
Title: Managing Director

Optional:
Company name: Brask and Partners Ltd.
Address: 1047 Budapest, Ravaszi str. 17/B, Hungary

Font styles to use
Other font styles liked:
• helveticaneue_medium, Prime Regular are used now.

Colors

Designer to choose colors to be used in the design.

Requirements
Must have
• I would like to have a 2 sided design.
Nice to have
• I thought if we make the logo a bit bigger (without the company name), that could go to the back with the company name below. I though, if the pipe in the logo is somehow touchable on the business card, would be nice and unique.

```html
<!DOCTYPE html>
<html lang="en">
<head>
<meta charset="utf-8">
<title>Brask and Partners – Business Card</title>
<link rel="stylesheet" href="https://fonts.googleapis.com/css2?family=Roboto:wght@400;500;700&display=swap">
<style>
  :root {
    --bg: #d9d9d9;
    --card-light: #ffffff;
    --card-dark: #262626;
    --magenta: #b3359f;
    --cyan: #1fa3e0;
    --grey: #5f5f5f;
    --ink: #2a2a2a;
    --muted: #8c7fa8;
    --white: #f2f2f2;
  }
  * { box-sizing: border-box; margin: 0; padding: 0; }
  html, body { width: 819px; height: 1200px; overflow: hidden; }
  body {
    background: var(--bg);
    font-family: "Roboto", "Helvetica Neue", Arial, sans-serif;
    display: flex;
    flex-direction: column;
    align-items: center;
    justify-content: center;
    gap: 64px;
  }
  .card {
    position: relative;
    width: 620px;
    height: 344px;
    overflow: hidden;
    box-shadow: 0 10px 28px rgba(0,0,0,.22);
  }
  .card--front { background: var(--card-light); }
  .card--back { background: var(--card-dark); color: var(--white); }

  .front__pattern {
    position: absolute;
    inset: 0;
    width: 100%;
    height: 100%;
  }
  .front__company {
    position: absolute;
    left: 62px;
    top: 236px;
  }
  .front__name {
    font-weight: 700;
    font-size: 15px;
    letter-spacing: 1.6px;
    text-transform: uppercase;
    color: var(--ink);
  }
  .front__address {
    margin-top: 6px;
    font-weight: 500;
    font-size: 10px;
    line-height: 1.35;
    color: var(--magenta);
  }

  .back__person {
    position: absolute;
    left: 58px;
    top: 46px;
  }
  .back__name {
    font-weight: 400;
    font-size: 25px;
  }
  .back__name .given { color: var(--magenta); }
  .back__name .family { color: var(--cyan); }
  .back__title {
    margin-top: 3px;
    font-size: 11px;
    font-weight: 500;
    color: var(--white);
  }
  .back__contact {
    position: absolute;
    left: 58px;
    top: 226px;
    list-style: none;
    font-size: 10.5px;
    line-height: 17px;
    color: var(--white);
  }
  .back__contact li {
    display: flex;
    align-items: center;
    gap: 12px;
  }
  .back__contact .dot {
    width: 6px;
    height: 6px;
    border-radius: 50%;
    background: var(--muted);
  }
  .back__brand {
    position: absolute;
    right: 46px;
    top: 148px;
    display: flex;
    align-items: center;
    gap: 10px;
  }
  .back__brand .mark {
    width: 14px;
    height: 14px;
    background: var(--magenta);
  }
  .back__brand .wordmark {
    font-size: 22px;
    font-weight: 400;
    color: var(--white);
  }
</style>
</head>
<body>

  <section class="card card--front" aria-label="Card front">
    <svg class="front__pattern" viewBox="0 0 620 344" role="img"
         aria-label="Brand symbol pattern of tilted magenta, cyan and grey squares across the upper right">
      <defs>
        <linearGradient id="patternTone" x1="0" y1="0" x2="1" y2="1">
          <stop offset="0" stop-color="#b3359f" stop-opacity=".28"/>
          <stop offset=".5" stop-color="#1fa3e0" stop-opacity=".28"/>
          <stop offset="1" stop-color="#5f5f5f" stop-opacity=".22"/>
        </linearGradient>
      </defs>
      <polygon points="150,0 620,0 620,300 560,344 470,344 340,200 240,120" fill="url(#patternTone)"/>
    </svg>
    <div class="front__company">
      <p class="front__name">Brask and Partners Ltd.</p>
      <p class="front__address">1047 Budapest, Ravaszi str.<br>17/B, Hungary</p>
    </div>
  </section>

  <section class="card card--back" aria-label="Card back">
    <div class="back__person">
      <p class="back__name"><span class="given">Gergely</span> <span class="family">Halmindo</span></p>
      <p class="back__title">Managing Director</p>
    </div>
    <div class="back__brand">
      <span class="mark"></span>
      <span class="wordmark">Brask &amp; Partners</span>
    </div>
    <ul class="back__contact">
      <li><span class="dot"></span>+36 30 555 0192</li>
      <li><span class="dot"></span>g.halmindo@braskpartnera.hu</li>
      <li><span class="dot"></span>www.braskpartnera.hu</li>
    </ul>
  </section>

</body>
</html>
```